N.5 HTML Media Template for Virtual Assistant card

We need the development of 5 interactive and optimized web card templates, each designed specifically for a different type of topic. These templates will initially be displayed in a chat client on both desktop and mobile devices, and subsequently shared across major social networks. The cards will serve as response balloons in the chat for queries related to various topics such as local business searches, news, history, sports, etc. Each template will be tailored to optimize the presentation of specific content for each topic.The goal is to create cards that capture user attention through engaging designs, easily readable text, and light animations, while ensuring excellent cross-platform compatibility and rapid loading speed both in the chat client context and across various social media video formats. The content of the cards should be designed to be effective in a chat card loop, providing an engaging and informative user experience.The cards will be used in specific video formats for platforms like Facebook Feed, Instagram Reels, YouTube Shorts, LinkedIn Video, and TikTok, with detailed technical specifications provided below. The project requires the use of modern web technologies, such as HTML5, inline CSS, and JavaScript, with a focus on performance optimization and adherence to web accessibility standards.

We require the development of a web page that meets the following criteria:

Responsive Design: The page must be optimized to adapt perfectly to the resolutions used by the most popular social networks, ensuring a smooth and consistent user experience on all devices (smartphones, tablets, desktops).
Text: The page should contain easily readable text, which may include rather lengthy texts.
Images: Inclusion of standard images and panoramic images (360 degrees).
Animations: Use lightweight animations to enhance interactivity without compromising page loading speed.
Inline Styles: Prefer the use of inline styles for better management and performance.
External Scripts: The use of external scripts is allowed as long as they are hosted on reliable CDNs. However, it's essential that these scripts are lightweight and do not negatively impact the page loading speed.

The page should be lightweight and designed with a strong focus on loading speed.
Implementation of optimization techniques such as lazy loading, image compression, and code minification.
The page must comply with web accessibility standards.
Ensure that all content is accessible and easily navigable.
The cards must be created in HTML5.
The CSS must be inline and compatible with:

last 1 Chrome version
last 1 Firefox version
last 2 Edge major versions
last 2 Safari major versions
last 2 iOS major versions
Firefox ESR
Inline JavaScript and fast CDN-loaded scripts are allowed and should be executed on 'DOMContentLoaded' of the card (include a loading spinner).
All cards must be responsive.
All cards must respond (via CSS media queries) to a specific format related to the social platform and the video format to be created.
List of social video formats:
Facebook Feed Video:
Recommended dimensions: 1280 x 720 pixels for both landscape and portrait
Minimum width: 1200 pixels
Supported ratios: 16:9 (landscape), 9:16 (full portrait)

Facebook Stories:
Recommended size: 1080 x 1080 pixels
Minimum size: 600 x 600 pixels (1:1 aspect ratio)
Aspect ratios: from 1.91 to 9:16, with gradient-colored bars above and below videos less than 9:16

Facebook Reels:
Resolution: minimum 540 x 960 (540p) (recommended 1080×1920 or higher)
Supported aspect ratios: 9:16

Instagram in-feed video:
Video landscape: 1920 by 1080 pixels (16:9 aspect ratio)
Square video: 1080 by 1080 pixels (1:1 aspect ratio)
Vertical video: 1080 by 1350 pixels (4:5 aspect ratio)

Instagram Reels:
Supported aspect ratios: 0.01:1-10:1 (9:16 recommended)

Instagram Stories Video:
Recommended size: 1080px by 1080px pixels
Minimum size: 600 x 1067

X landscape videos:
Recommended size: 1280 by 720 pixels
Supported aspect ratios: 16:9

X Portrait and Square Videos:
Recommended sizes: 720×1280 (portrait), 720 by 720 pixels (square)

YouTube Video:
Recommended sizes:
426 by 240 pixels (240p)
640 by 360 pixels (360p)
854 by 480 pixels (480p)
1280 by 720 pixels (720p)
1920 by 1080 pixels (1080p)
2560 by 1440 pixels (1440p)
3840 by 2160 pixels (2160p)
Supported aspect ratios: 16:9 and 4:3

YouTube Shorts:
Recommended sizes:
240 by 426 pixels (240p)
360 by 640 pixels (360p)
480 by 854 pixels (480p)
720 by 1280 pixels (720p)

LinkedIn Video:
Maximum size: 4,096 by 2,304 pixels
Supported aspect ratios: from 1:2.4 to 2.4:1

TikTok:
Format 9:16 (portrait)
Recommended dimensions: 1920 by 1080 pixels (1080p)

We need the UI and implementation of 5 cards with animations, which will first be inserted into a virtual assistant chat (like lumo talk), and then shared on social networks as videos(Our system generates an mp4 of the animation). The cards contain images (from google image API), text and 360-degree overviews, for local activities for example. We need them to be designed according to the type of information they contain, so with different animations depending on the type of card. Example: a response that contains 1) card about a business (as in the figma I sent you), or a response that contains 2) information about a sporting event (images attached), 3) Web search, 4) News, 5) product card. The cards should have the characteristics indicated in the brief .The images we have available, related to the responses in the chat, are generated via real-time api calls, along with the ai responses, cannot be edited or cropped, and are often small in size.

The attached figma and video and pictures are just an example to make it clear what they are for. We want creative design that is not something already seen and traditional. Be creative.

https://www.plandeskio.example/view/Xq82Lm4TrVw9PzKd1/OKTRA-TILE?sheet=1&frame=412-7781&zoom=0.5

https://www.plandeskio.example/view/Xq82Lm4TrVw9PzKd1/OKTRA-TILE?sheet=1&frame=412-7902&zoom=0.5&mode=edit

In attachment, a very ugly and rudimentary example
Updates

Low design quality

Low design quality

Low design quality

Target Market(s)

B2C

Industry/Entity Type

media content

Coding

Coded - Design and coding required

Colors
00AB8E
00BBA5
67D7C9
C6EFE9
E9F9F6

Requirements
Must have
• Innovative, Engaging
Nice to have
• Card not seen before
Should not have
• Traditional card

```html
<!DOCTYPE html>
<html lang="en">
<head>
<meta charset="utf-8">
<title>Orvel Chat Cards</title>
<link rel="stylesheet" href="https://fonts.googleapis.com/css2?family=Montserrat:wght@400;500;600;700;800&display=swap">
<style>
:root{
  --stage:#2f2f2f;
  --teal:#2a989b;
  --teal-icon:#2fb0b2;
  --teal-soft:#dcefee;
  --white:#ffffff;
  --ink:#1d1d1d;
  --muted:#3a3a3a;
  --red:#f2493a;
  --red-soft:#f66a5c;
  --star:#f09a12;
  --pill:#eeeeee;
}
*{box-sizing:border-box;margin:0;padding:0}
html,body{width:1200px;height:698px;overflow:hidden;background:var(--stage)}
body{position:relative;font-family:"Montserrat",sans-serif;color:var(--ink)}
.abs{position:absolute}

/* Sidebar */
.sidebar{left:38px;top:36px;width:294px;height:632px;background:var(--teal);color:var(--white)}
.brand{position:absolute;left:0;right:0;top:20px;text-align:center;font-weight:700}
.brand-line{font-size:19px;line-height:1.3}
.thread{position:absolute;left:0;width:294px;height:50px}
.thread-avatar{position:absolute;left:29px;top:0;width:46px;height:46px;border-radius:50%;background:var(--teal-icon);display:flex;align-items:center;justify-content:center}
.thread-title{position:absolute;left:84px;top:-4px;font-size:11.2px;font-weight:800;white-space:nowrap}
.thread-text{position:absolute;left:84px;top:14px;font-size:9.6px;font-weight:500;line-height:13.8px;white-space:nowrap}
.thread-time{position:absolute;left:245px;top:-1px;font-size:11px;font-weight:600}
.thread-pin{position:absolute;left:255px;top:22px;opacity:.55}
.sidebar-actions{position:absolute;left:192px;bottom:26px;display:flex;gap:10px}
.round-btn{width:31px;height:31px;border-radius:50%;background:var(--teal-icon);display:flex;align-items:center;justify-content:center}

/* Chat */
.chat{left:332px;top:36px;width:590px;height:632px;background:var(--white)}
.chat-bar{position:absolute;left:0;top:0;width:590px;height:40px;background:var(--white);box-shadow:0 6px 14px rgba(0,0,0,.05)}
.chat-bar-icon{position:absolute;left:108px;top:11px}
.chat-bar-text{position:absolute;left:137px;top:14px;font-size:9.2px;font-weight:500;white-space:nowrap}
.menu-pill{position:absolute;left:518px;top:9px;width:59px;height:21px;border-radius:11px;background:var(--pill);display:flex;align-items:center;justify-content:center;gap:5px;font-size:7.6px;font-weight:700}
.msg-date{position:absolute;left:362px;top:67px;font-size:9.6px;font-weight:500}
.msg-bubble{position:absolute;left:354px;top:87px;width:200px;height:63px;background:var(--teal);color:var(--white);font-size:9.6px;font-weight:500;line-height:15px;padding:15px 14px}
.media-frame{position:absolute;left:24px;top:195px;width:539px;height:399px;border-radius:30px;background:var(--white);box-shadow:0 2px 8px rgba(0,0,0,.12)}
.media-photo{position:absolute;left:5px;top:5px;width:529px;height:389px;border-radius:25px;overflow:hidden;
  background:radial-gradient(ellipse at 50% 20%,#8fb3ad 0%,#3d6b6e 30%,#1f3a40 60%,#1b2a26 100%)}
.media-photo::after{content:"";position:absolute;inset:0;background:linear-gradient(180deg,rgba(0,0,0,0) 45%,rgba(20,35,20,.55) 80%,rgba(10,20,12,.85) 100%)}
.media-headline{position:absolute;left:21px;top:200px;z-index:1;color:var(--white);font-size:30.5px;font-weight:700;line-height:38px;letter-spacing:-.2px;white-space:nowrap}
.media-tabs{position:absolute;left:23px;top:338px;z-index:1;display:flex;gap:17px;color:var(--white);font-size:11px;font-weight:700;white-space:nowrap}
.action-rail{position:absolute;background:var(--red);border-radius:20px;display:flex;flex-direction:column;align-items:center}
.chat .action-rail{left:536px;top:333px;width:37px;height:148px;padding-top:9px;gap:12.5px}
.action-dot{width:23px;height:23px;border-radius:50%;background:var(--red-soft);display:flex;align-items:center;justify-content:center}
.action-dot.on{background:var(--white)}

/* Mobile card */
.mobile{left:952px;top:36px;width:210px;height:405px;background:var(--white);overflow:hidden}
.mobile::before{content:"";position:absolute;left:-40px;top:60px;width:180px;height:260px;border-radius:50%;background:#f2f4f4}
.mobile-brand{position:absolute;left:0;right:0;top:14px;text-align:center;font-weight:700}
.mobile-brand .brand-line{font-size:11px;line-height:1.3}
.venue-ring{position:absolute;left:25px;top:55px;width:160px;height:160px;border-radius:50%;background:var(--teal-soft)}
.venue-photo{position:absolute;left:34px;top:64px;width:142px;height:142px;border-radius:50%;
  background:radial-gradient(circle at 55% 35%,#e8c49a 0%,#a4693e 35%,#6b3d24 70%,#4a2a1a 100%)}
.mobile .action-rail{left:176px;top:86px;width:22px;height:97px;padding-top:4px;gap:9px}
.mobile .action-dot{width:15px;height:15px}
.rating{position:absolute;left:0;right:0;top:231px;display:flex;justify-content:center;gap:4px}
.venue-text{position:absolute;left:12px;width:186px;top:252px;text-align:center;font-size:7px;line-height:14.2px;color:var(--muted)}
.chip-row{position:absolute;left:0;right:0;display:flex;justify-content:center;gap:6px}
.chip{height:15px;padding:0 7px;border-radius:8px;background:var(--red);color:var(--white);font-size:5.4px;font-weight:700;display:flex;align-items:center;white-space:nowrap}
</style>
</head>
<body>
<svg width="0" height="0" style="position:absolute" aria-hidden="true">
  <defs>
    <symbol id="i-chat" viewBox="0 0 24 20">
      <path d="M9 1C4.6 1 1 3.8 1 7.2c0 1.9 1.1 3.6 2.8 4.7L3 15l3.5-1.9c.8.2 1.6.3 2.5.3 4.4 0 8-2.8 8-6.2S13.4 1 9 1z"/>
      <path d="M18.5 7.5c.1.3.1.6.1.9 0 4-4 7.1-8.6 7.3 1.3 1.3 3.4 2.1 5.7 2.1.7 0 1.4-.1 2-.2L20.8 19l-.6-2.7c1.6-1 2.7-2.5 2.7-4.2 0-1.8-1.7-3.5-4.4-4.6z"/>
    </symbol>
    <symbol id="i-pin" viewBox="0 0 16 16"><path d="M10 1l5 5-2 1-3 3 .5 3.5L9 15l-3-3-4 4-1-1 4-4-3-3 1.5-1.5L7 6l3-3z"/></symbol>
    <symbol id="i-phone" viewBox="0 0 16 16"><path d="M4 1.5l2 3-1.3 1.6c.8 1.8 2.4 3.4 4.2 4.2L10.5 9l3 2-.8 2.6c-.3.8-1.1 1.1-1.9.9C6.6 13.2 2.8 9.4 1.5 5.2c-.2-.8.1-1.6.9-1.9z"/></symbol>
    <symbol id="i-mail" viewBox="0 0 16 16"><path d="M1.5 3.5h13v9h-13z"/><path d="M1.5 4l6.5 5 6.5-5" fill="none" stroke="#f66a5c" stroke-width="1.2"/></symbol>
    <symbol id="i-globe" viewBox="0 0 16 16"><circle cx="8" cy="8" r="6.5"/><path d="M5 5.5c1.5-.5 2.5.5 2 1.7-.6 1.3 1 2.2.5 3.8M10 3.5c-.3 1.2.7 1.8 1.8 1.5" fill="none" stroke="#f66a5c" stroke-width="1.1"/></symbol>
    <symbol id="i-share" viewBox="0 0 16 16"><circle cx="12" cy="3.5" r="2.3"/><circle cx="4" cy="8" r="2.3"/><circle cx="12" cy="12.5" r="2.3"/><path d="M4 8l8-4.5M4 8l8 4.5" stroke="#fff" stroke-width="1.4"/></symbol>
    <symbol id="i-star" viewBox="0 0 16 16"><path d="M8 1l2.1 4.5 4.9.6-3.6 3.3 1 4.8L8 11.8 3.6 14.2l1-4.8L1 6.1l4.9-.6z"/></symbol>
  </defs>
</svg>

<aside class="abs sidebar" aria-label="Conversations">
  <header class="brand">
    <div class="brand-line">Orvel</div>
    <div class="brand-line">Chat Cards</div>
  </header>

  <div class="thread" style="top:128px">
    <div class="thread-avatar"><svg width="22" height="19" fill="#fff"><use href="#i-chat"/></svg></div>
    <div class="thread-title">Lorem Ipsum</div>
    <p class="thread-text">Lorem ipsum dolor sit amet,<br>consectetur adipiscing elit, sed do</p>
    <div class="thread-time">16:24</div>
    <svg class="thread-pin" width="10" height="10" fill="#fff"><use href="#i-pin"/></svg>
  </div>
  <div class="thread" style="top:204px">
    <div class="thread-avatar"><svg width="22" height="19" fill="#fff"><use href="#i-chat"/></svg></div>
    <div class="thread-title">Lorem Ipsum</div>
    <p class="thread-text">Lorem ipsum dolor sit amet,<br>consectetur adipiscing elit, sed do</p>
    <div class="thread-time">16:24</div>
    <svg class="thread-pin" width="10" height="10" fill="#fff"><use href="#i-pin"/></svg>
  </div>
  <div class="thread" style="top:275px">
    <div class="thread-avatar"><svg width="22" height="19" fill="#fff"><use href="#i-chat"/></svg></div>
    <div class="thread-title">Lorem Ipsum</div>
    <p class="thread-text">Lorem ipsum dolor sit amet,<br>consectetur adipiscing elit, sed do</p>
    <div class="thread-time">16:24</div>
    <svg class="thread-pin" width="10" height="10" fill="#fff"><use href="#i-pin"/></svg>
  </div>
  <div class="thread" style="top:345px">
    <div class="thread-avatar"><svg width="22" height="19" fill="#fff"><use href="#i-chat"/></svg></div>
    <div class="thread-title">Lorem Ipsum</div>
    <p class="thread-text">Lorem ipsum dolor sit amet,<br>consectetur adipiscing elit, sed do</p>
    <div class="thread-time">16:24</div>
    <svg class="thread-pin" width="10" height="10" fill="#fff"><use href="#i-pin"/></svg>
  </div>
  <div class="thread" style="top:415px">
    <div class="thread-avatar"><svg width="22" height="19" fill="#fff"><use href="#i-chat"/></svg></div>
    <div class="thread-title">Lorem Ipsum</div>
    <p class="thread-text">Lorem ipsum dolor sit amet,<br>consectetur adipiscing elit, sed do</p>
    <div class="thread-time">16:24</div>
    <svg class="thread-pin" width="10" height="10" fill="#fff"><use href="#i-pin"/></svg>
  </div>
  <div class="thread" style="top:483px">
    <div class="thread-avatar"><svg width="22" height="19" fill="#fff"><use href="#i-chat"/></svg></div>
    <div class="thread-title">Lorem Ipsum</div>
    <p class="thread-text">Lorem ipsum dolor sit amet,<br>consectetur adipiscing elit, sed do</p>
    <div class="thread-time">16:24</div>
    <svg class="thread-pin" width="10" height="10" fill="#fff"><use href="#i-pin"/></svg>
  </div>

  <div class="sidebar-actions">
    <div class="round-btn" aria-label="Cards">
      <svg width="16" height="12" viewBox="0 0 16 12" fill="none" stroke="#fff" stroke-width="1.2"><rect x="1" y="1" width="14" height="10" rx="1"/><rect x="3" y="3" width="4" height="4"/><path d="M9 3.5h4M9 5.5h4M3 8.5h10"/></svg>
    </div>
    <div class="round-btn" aria-label="New conversation">
      <svg width="13" height="13" viewBox="0 0 13 13" stroke="#fff" stroke-width="2"><path d="M6.5 1v11M1 6.5h11"/></svg>
    </div>
  </div>
</aside>

<main class="abs chat">
  <div class="chat-bar">
    <svg class="chat-bar-icon" width="19" height="16" fill="var(--teal)"><use href="#i-chat"/></svg>
    <span class="chat-bar-text">Lorem ipsum dolor sit amet,consectetur adipiscing elit, sed do</span>
    <div class="menu-pill">
      <svg width="8" height="7" viewBox="0 0 8 7" fill="var(--teal)"><rect width="8" height="1.4"/><rect y="2.8" width="8" height="1.4"/><rect y="5.6" width="8" height="1.4"/></svg>
      Menu
    </div>
  </div>

  <div class="msg-date">18 12 2023 16:24</div>
  <div class="msg-bubble">Lorem ipsum dolor sit amet, consectetur adipiscing elit, sed do</div>

  <section class="media-frame" aria-label="Sporting event card">
    <div class="media-photo" role="img" aria-label="Photo of a football player in a floodlit stadium full of fans"></div>
    <h2 class="media-headline">Lorem ipsum dolor<br>sit amet, consectetur<br>adipiscing elit, sed do</h2>
    <nav class="media-tabs">
      <span>Card About a Business</span>
      <span>Sporting Event</span>
      <span>Web search</span>
      <span>News</span>
      <span>Product Card</span>
    </nav>
  </section>

  <div class="action-rail">
    <div class="action-dot on"><svg width="10" height="10" fill="var(--teal)"><use href="#i-phone"/></svg></div>
    <div class="action-dot"><svg width="10" height="10" fill="#fff"><use href="#i-mail"/></svg></div>
    <div class="action-dot"><svg width="10" height="10" fill="#fff"><use href="#i-globe"/></svg></div>
    <div class="action-dot"><svg width="10" height="10" fill="#fff"><use href="#i-share"/></svg></div>
  </div>
</main>

<section class="abs mobile" aria-label="Business card, mobile">
  <header class="mobile-brand">
    <div class="brand-line">Orvel</div>
    <div class="brand-line">Chat Cards</div>
  </header>
  <div class="venue-ring"></div>
  <div class="venue-photo" role="img" aria-label="Photo of a warm wooden restaurant interior with tables and pendant lamps"></div>
  <div class="action-rail">
    <div class="action-dot on"><svg width="7" height="7" fill="var(--teal)"><use href="#i-phone"/></svg></div>
    <div class="action-dot"><svg width="7" height="7" fill="#fff"><use href="#i-mail"/></svg></div>
    <div class="action-dot"><svg width="7" height="7" fill="#fff"><use href="#i-globe"/></svg></div>
    <div class="action-dot"><svg width="7" height="7" fill="#fff"><use href="#i-share"/></svg></div>
  </div>
  <div class="rating" aria-label="Rated 3 out of 5">
    <svg width="10" height="10" fill="var(--star)"><use href="#i-star"/></svg>
    <svg width="10" height="10" fill="var(--star)"><use href="#i-star"/></svg>
    <svg width="10" height="10" fill="var(--star)"><use href="#i-star"/></svg>
    <svg width="10" height="10" fill="none" stroke="var(--star)" stroke-width="1.4"><use href="#i-star"/></svg>
    <svg width="10" height="10" fill="none" stroke="var(--star)" stroke-width="1.4"><use href="#i-star"/></svg>
  </div>
  <p class="venue-text">Lorem ipsum dolor sit amet, consectetur<br>adipiscing elit, sed do eiusmod tempor<br>incididunt ut labore et dolore magna aliqua.<br>Quis ipsum suspendisse ultrices gravida. Risus<br>commodo viverra maecenas accumsan lacus<br>vel facilisis.</p>
  <div class="chip-row" style="top:350px">
    <span class="chip">Card About a Business</span>
    <span class="chip">Sporting Event</span>
  </div>
  <div class="chip-row" style="top:373px">
    <span class="chip">Web Search</span>
    <span class="chip">News</span>
    <span class="chip">Product Card</span>
  </div>
</section>
</body>
</html>
```